Bellcrest HVAC Business Card design

Looking for a modern professional two sided design. Showing contact info and services provided. Possibly on a silk card stock.
Using blues or greens or greys and maybe metallic. One color or a mixture of these.
Dorian Vance
dvance@bellcresthvac-example.net
555-318-4702
Air Conditioning
Heating
Heat Pumps / Gas / Oil
Ductless mini splits
Controls
VFD's
Pumps
Gas Fitting/Piping
Service and New install
Residential / Commercial
Industry/Entity Type
Mechanical HVAC
Contact Information for Business Card
Logo, contact info and provided services

```html
<!DOCTYPE html>
<html lang="en">
<head>
<meta charset="utf-8">
<title>Bellcrest HVAC Business Card</title>
<link href="https://fonts.googleapis.com/css2?family=Open+Sans:wght@400;600;700;800&display=swap" rel="stylesheet">
<style>
  :root {
    --stage: #232323;
    --card-front: #1277c4;
    --card-back: #1f1f22;
    --brand-blue: #1a78c8;
    --text-light: #ffffff;
    --front-type: #cfe6fa;
  }
  * { box-sizing: border-box; margin: 0; padding: 0; }
  html, body { width: 1200px; height: 780px; overflow: hidden; background: var(--stage); }
  body { font-family: "Open Sans", sans-serif; position: relative; }

  .card {
    position: absolute;
    top: 80px;
    width: 360px;
    height: 620px;
    border-radius: 24px;
    box-shadow: 0 14px 30px rgba(0,0,0,.55);
    overflow: hidden;
  }
  .card--front { left: 200px; background: var(--card-front); display: flex; align-items: center; justify-content: center; }
  .card--back { left: 640px; background: var(--card-back); }

  .front-name {
    color: var(--front-type);
    font-weight: 800;
    font-size: 48px;
    line-height: 1.1;
    text-align: center;
    letter-spacing: 1px;
  }

  .back-name {
    position: absolute; top: 48px; left: 0; right: 0;
    text-align: center; color: var(--brand-blue);
    font-weight: 800; font-size: 30px; letter-spacing: .5px;
  }

  .person { position: absolute; top: 130px; left: 0; right: 0; text-align: center; }
  .person__name { color: var(--brand-blue); font-weight: 800; font-size: 36px; line-height: 1.1; }
  .person__title { color: var(--text-light); font-weight: 600; font-size: 16px; margin-top: 2px; }

  .frame { position: absolute; inset: 0; pointer-events: none; }

  .icons { position: absolute; top: 212px; left: 0; right: 0; display: flex; justify-content: center; gap: 22px; }
  .icon { width: 30px; height: 30px; border-radius: 50%; background: var(--brand-blue); display: flex; align-items: center; justify-content: center; }

  .contact { position: absolute; top: 262px; left: 0; right: 0; text-align: center; color: var(--text-light); font-size: 14.5px; line-height: 22px; font-weight: 600; }

  .services-label {
    position: absolute; top: 352px; left: 50%; transform: translateX(-50%);
    background: var(--brand-blue); color: var(--text-light);
    font-weight: 800; font-size: 17px; letter-spacing: .5px;
    padding: 4px 28px; border-radius: 20px;
  }

  .services {
    position: absolute; top: 400px; left: 34px; right: 34px; height: 196px;
    border: 2px solid var(--brand-blue);
    padding: 10px 18px;
    list-style: none;
    color: var(--text-light); font-size: 15px; line-height: 22px; font-weight: 600;
  }
  .services li::before, .services .dot { content: ""; }
  .dot { display: inline-block; width: 8px; height: 8px; border-radius: 50%; background: var(--brand-blue); margin-right: 7px; vertical-align: 1px; }
</style>
</head>
<body>

<section class="card card--front" aria-label="Card front">
  <div class="front-name">Bellcrest<br>HVAC</div>
</section>

<section class="card card--back" aria-label="Card back">
  <div class="back-name">Bellcrest HVAC</div>

  <div class="person">
    <div class="person__name">Dorian Vance</div>
    <div class="person__title">Director</div>
  </div>

  <svg class="frame" width="360" height="620" viewBox="0 0 360 620">
    <g fill="none" stroke="#1a78c8" stroke-width="2">
      <polyline points="115,227 28,227 28,330 52,330"/>
      <polyline points="245,227 332,227 332,300 310,300"/>
      <line x1="180" y1="244" x2="180" y2="256"/>
      <line x1="180" y1="382" x2="180" y2="396"/>
    </g>
    <g fill="#1a78c8">
      <polygon points="58,330 50,325 50,335"/>
      <polygon points="304,300 312,295 312,305"/>
      <polygon points="180,262 175,254 185,254"/>
      <polygon points="180,400 175,392 185,392"/>
    </g>
  </svg>

  <div class="icons">
    <span class="icon" aria-label="Email">
      <svg width="16" height="12" viewBox="0 0 16 12"><rect x="1" y="1" width="14" height="10" fill="none" stroke="#fff" stroke-width="1.5"/><polyline points="1,1 8,7 15,1" fill="none" stroke="#fff" stroke-width="1.5"/></svg>
    </span>
    <span class="icon" aria-label="Phone">
      <svg width="14" height="14" viewBox="0 0 24 24"><path fill="#fff" d="M6.6 10.8a15 15 0 0 0 6.6 6.6l2.2-2.2c.3-.3.7-.4 1-.2 1.1.4 2.3.6 3.6.6.6 0 1 .4 1 1V20c0 .6-.4 1-1 1A17 17 0 0 1 3 4c0-.6.4-1 1-1h3.5c.6 0 1 .4 1 1 0 1.3.2 2.5.6 3.6.1.3 0 .7-.2 1z"/></svg>
    </span>
    <span class="icon" aria-label="Website">
      <svg width="16" height="16" viewBox="0 0 16 16" fill="none" stroke="#fff" stroke-width="1.3"><circle cx="8" cy="8" r="6.5"/><ellipse cx="8" cy="8" rx="3" ry="6.5"/><line x1="1.5" y1="8" x2="14.5" y2="8"/></svg>
    </span>
  </div>

  <div class="contact">
    <div>555-318-4702</div>
    <div>dvance@bellcresthvac-example.net</div>
    <div>www.bellcresthvac-example.net</div>
  </div>

  <div class="services-label">SERVICES</div>

  <ul class="services">
    <li><span class="dot"></span>VFD's <span class="dot"></span>Pumps</li>
    <li><span class="dot"></span>Heating <span class="dot"></span>Controls</li>
    <li><span class="dot"></span>Air Conditioning</li>
    <li><span class="dot"></span>Gas Fitting/Piping</li>
    <li><span class="dot"></span>Ductless mini splits</li>
    <li><span class="dot"></span>Heat Pumps / Gas / Oil</li>
    <li><span class="dot"></span>Service and New install</li>
    <li><span class="dot"></span>Residential / Commercial</li>
  </ul>
</section>

</body>
</html>
```